Online Prescription Eyewear Company Needs a Website

We sell prescription glasses starting at $99 with Free Shipping. We have over 300 different styles and colors.

Our website is under construction and we need an amazing landing page to kick things off. Our brand is called VORAN and our website is called VORANEYEWEAR.COM.

We are a website similar to
tendrilcove.com
shopbrantholm.com
Quopa.com

We sell prescription glasses starting at $99 with Free Shipping. Options to upgrade to Anti Glare, Blue light Protection, Transitions or High Index.

We also have a lens replacement option and will change out old prescription lenses starting at $79 with Free Shipping.

Important!!

We Love the layout of https://dunsteroak.com/ . We are hoping to use Dunster Oak as a templet. The closest page that looks like Dunster Oak will win.

We do not prefer the pink. Substitute the pink with Navy Teal.

We also prefer a better footer than Dunster Oak

The landing page should include, Gender neutral and Colors are Black, White, Gray, Navy Teal

We prefer a Simple, Clean Look.

The Header should be similar to tendrilcove.com

The Landing page look very similar to Dunster Oak with large banner with quad banner below to follow.

We need better footer. Here are the menu items for footer.

PRODUCTS
All Frames
Mens Frames
Womens Frames
Best Sellers
New Arrivals

ORDER
Single Vision Lenses
Blue Light Blocking Computer Lenses
High Index Lenses
Transition Lenses
Reading Lenses

INFORMATION
Track Order
About Us
Contact Us
Returns
Warranty
FAQ

Target Market(s)

20-40 yo Male/Female wears glasses

Industry/Entity Type

Eyewear

Number of Pages Required

1 page

Font styles to use
Sans Serif

Colors
333333
5c5c5c
919191
b2b2b2
dfdfdf
f5f5f5
1b1b1b
474747
3276b5

Requirements
Must have
• The Landing page look very similar to Dunster Oak.
• Substitute the pink secondary color for Navy Teal
• Should have main Banner with Person wearing glasses. Then the quad banner below should highlight the box with glasses, glasses, etc.
Nice to have
• i have a pixel barn account, so if you find some awesome pictures I can purchase them if they fit in the site.

```html
<!DOCTYPE html>
<html lang="en">
<head>
<meta charset="utf-8">
<title>VORAN — Prescription Eyewear</title>
<link rel="stylesheet" href="https://fonts.googleapis.com/css2?family=Roboto:wght@300;400;500;700;900&family=Lato:wght@400;700&display=swap">
<style>
:root{
  --ink:#1b1b1b;
  --dark:#333333;
  --mid:#474747;
  --grey:#5c5c5c;
  --soft:#919191;
  --line:#b2b2b2;
  --pale:#dfdfdf;
  --mist:#f5f5f5;
  --white:#ffffff;
  --teal:#3276b5;
  --star:#f2a516;
  --red:#d8302f;
}
*{margin:0;padding:0;box-sizing:border-box}
html,body{width:1200px;height:3727px;overflow:hidden}
body{position:relative;background:var(--white);font-family:"Lato",sans-serif;color:var(--dark)}
.abs{position:absolute}
.btn{position:absolute;background:var(--teal);color:var(--white);border-radius:17px;font:700 15px "Lato",sans-serif;display:flex;align-items:center;justify-content:center;text-decoration:none}
.photo{position:absolute}

/* header */
.site-header{position:absolute;left:0;top:0;width:1200px;height:85px;background:var(--white)}
.menu-icon{left:118px;top:34px}
.brand{position:absolute;left:0;width:1200px;top:22px;text-align:center;font:300 34px "Roboto",sans-serif;letter-spacing:5px;color:var(--ink)}
.cart{left:1034px;top:28px;display:flex;align-items:center;gap:6px;font:400 14px "Lato",sans-serif;color:var(--ink)}

/* hero */
.hero{left:0;top:85px;width:1200px;height:623px;
  background:
    radial-gradient(ellipse 22% 38% at 78% 42%,rgba(236,200,178,.95),rgba(236,200,178,0) 70%),
    radial-gradient(ellipse 30% 30% at 88% 12%,rgba(238,232,224,.9),rgba(238,232,224,0) 70%),
    radial-gradient(ellipse 14% 10% at 80% 34%,rgba(30,30,30,.55),rgba(30,30,30,0) 80%),
    radial-gradient(ellipse 40% 60% at 20% 40%,rgba(160,110,80,.7),rgba(160,110,80,0) 70%),
    linear-gradient(100deg,#5a3d2e 0%,#8c6248 28%,#b89076 52%,#d9b9a2 72%,#c8a48c 100%)}
.hero-title{left:119px;top:330px;font:400 55px/66px "Roboto",sans-serif;color:var(--white)}
.hero-title b{font-weight:700}

/* category banners */
.category{top:758px;width:532px;height:464px;overflow:hidden}
.category .band{position:absolute;left:0;bottom:0;width:100%;height:67px;background:rgba(50,118,181,.88);color:var(--white);font:700 28px "Roboto",sans-serif;display:flex;align-items:center;justify-content:center}

/* featured */
.section-title{font:400 30px "Roboto",sans-serif;color:var(--ink)}
.tabs{left:0;width:1200px;top:1338px;text-align:center;font:400 15px "Lato",sans-serif;color:var(--grey)}
.tabs span{margin:0 20px}
.tabs .active{color:var(--teal);font-weight:700}
.tabs .sep{color:var(--soft);margin:0}
.arrow-btn{width:26px;height:26px;border:2px solid var(--teal);border-radius:50%;display:flex;align-items:center;justify-content:center}
.product{top:1387px;width:256px;height:261px;background:var(--mist)}
.product .frame{position:absolute;left:0;top:40px;width:256px;height:150px}
.product-meta{top:1668px;width:256px;text-align:center;font:400 15px/26px "Lato",sans-serif;color:var(--mid)}
.product-meta b{color:var(--ink)}
.tool{position:absolute;top:196px;width:36px;height:36px;border-radius:50%;background:var(--teal);display:flex;align-items:center;justify-content:center}

/* lens offer */
.lens-offer{left:0;top:1849px;width:1200px;height:452px;background:var(--mist)}
.lens-title{left:119px;top:1978px;font:700 42px "Roboto",sans-serif;color:var(--ink)}
.lens-sub{left:119px;top:2028px;font:400 34px "Roboto",sans-serif;color:var(--ink)}
.lens-price{left:119px;top:2068px;font:700 50px "Roboto",sans-serif;color:var(--teal)}
.lens-photo{left:497px;top:1945px;width:621px;height:262px;
  background:
    radial-gradient(ellipse 40% 22% at 70% 80%,rgba(200,205,210,.9),rgba(200,205,210,0) 75%),
    radial-gradient(ellipse 48% 34% at 50% 30%,rgba(60,55,52,.55),rgba(60,55,52,0) 75%),
    linear-gradient(180deg,rgba(245,245,245,0),rgba(245,245,245,0))}

/* reviews */
.review-card{left:75px;top:2425px;width:487px;height:445px;background:var(--mist)}
.avatar{left:250px;top:2464px;width:134px;height:134px;border-radius:50%;
  background:radial-gradient(circle at 50% 40%,#e7c2ad,#c28f78 55%,#7d5a4a);border:3px solid var(--white)}
.reviewer{left:75px;width:487px;text-align:center}
.quote{font:700 48px/48px "Roboto",sans-serif;color:var(--ink)}
.dots{left:293px;top:2798px;display:flex;gap:6px}
.dots i{width:7px;height:7px;border-radius:50%;background:var(--line)}
.dots i.on{background:var(--red)}

/* blog */
.post{left:611px;width:507px;height:172px;background:var(--mist)}
.post .thumb{position:absolute;left:18px;top:18px;width:166px;height:140px}
.post h3{position:absolute;left:202px;top:12px;font:400 20px "Roboto",sans-serif;color:var(--ink)}
.post .by{position:absolute;left:202px;top:44px;width:290px;display:flex;justify-content:space-between;font:400 12px "Lato",sans-serif;color:var(--ink)}
.post p{position:absolute;left:202px;top:66px;width:292px;font:400 13px/17px "Lato",sans-serif;color:var(--mid)}
.post .more{position:absolute;left:202px;top:136px;font:400 13px "Lato",sans-serif;color:var(--mid);display:flex;align-items:center;gap:4px}

/* newsletter */
.news-title{left:0;width:1200px;top:2926px;text-align:center;font:500 26px "Roboto",sans-serif;color:var(--ink)}
.news-sub{left:0;width:1200px;top:2962px;text-align:center;font:400 14px "Lato",sans-serif;color:var(--mid)}
.news-form{left:333px;top:2999px;width:512px;height:31px;background:var(--mist);border-radius:16px;overflow:hidden}
.news-form span{position:absolute;left:22px;top:8px;font:400 13px "Lato",sans-serif;color:var(--grey)}
.news-form b{position:absolute;right:0;top:0;width:132px;height:31px;background:var(--teal);color:var(--white);font:400 13px "Lato",sans-serif;display:flex;align-items:center;justify-content:center}

/* services */
.service{top:3101px;height:174px;background:var(--mist);text-align:center}
.service.featured{background:var(--teal)}
.service h4{position:absolute;left:0;width:100%;top:92px;font:700 17px "Lato",sans-serif;color:var(--mid)}
.service p{position:absolute;left:0;width:100%;top:118px;font:italic 400 13px "Lato",sans-serif;color:var(--mid)}
.service.featured h4,.service.featured p{color:var(--white)}

/* footer */
.site-footer{left:0;top:3347px;width:1200px;height:326px;background:var(--dark);color:var(--white)}
.foot-brand{left:119px;top:3432px;font:300 38px "Roboto",sans-serif;letter-spacing:6px}
.foot-about{left:119px;top:3498px;width:262px;font:400 13px/17px "Lato",sans-serif}
.cards{left:119px;top:3578px;display:flex;gap:6px}
.cards i{width:44px;height:28px;border-radius:3px;background:var(--pale)}
.foot-head{top:3438px;font:700 16px "Lato",sans-serif}
.foot-head::after{content:"";display:block;width:60px;height:2px;background:var(--white);margin-top:14px}
.foot-list{top:3494px;list-style:none;font:400 14px/19px "Lato",sans-serif}
.foot-list li::before{content:"•";margin-right:7px}
.addr{top:3494px;font:400 14px/21px "Lato",sans-serif}
.addr div{display:flex;align-items:flex-start;gap:9px}
.field{position:absolute;background:var(--grey);font:400 12px "Lato",sans-serif;color:var(--white);padding:5px 8px}
.send{left:974px;top:3583px;width:102px;height:22px;border-radius:11px;background:var(--teal);font:700 11px "Lato",sans-serif;display:flex;align-items:center;justify-content:center}
.copyright{left:118px;top:3693px;font:400 14px "Lato",sans-serif;color:var(--ink)}
.social{left:892px;top:3689px;display:flex;gap:10px}
.social i{width:25px;height:25px;border-radius:50%;background:var(--ink)}
</style>
</head>
<body>

<header class="site-header">
  <svg class="abs menu-icon" width="22" height="18" viewBox="0 0 22 18"><rect y="1" width="22" height="2.5" fill="#1b1b1b"/><rect y="7.5" width="22" height="2.5" fill="#1b1b1b"/><rect y="14" width="22" height="2.5" fill="#1b1b1b"/></svg>
  <div class="brand">VORAN</div>
  <div class="abs cart">
    <svg width="24" height="24" viewBox="0 0 24 24" fill="none" stroke="#1b1b1b" stroke-width="1.8"><path d="M4 8h16l-1.5 13h-13z"/><path d="M8 10V6a4 4 0 0 1 8 0v4"/></svg>
    <span>(0)</span>
  </div>
</header>

<section class="photo hero" role="img" aria-label="Woman with light hair wearing dark-rimmed prescription glasses, softly blurred city background"></section>
<h1 class="abs hero-title">Glasses Starting<br><b>at $99</b></h1>
<a class="btn" style="left:119px;top:470px;width:189px;height:33px">Shop Now</a>

<section class="abs category" style="left:45px">
  <div class="photo" style="inset:0;background:
    radial-gradient(ellipse 30% 24% at 55% 28%,rgba(214,170,140,.9),rgba(214,170,140,0) 75%),
    radial-gradient(ellipse 55% 40% at 50% 95%,rgba(34,52,96,.95),rgba(34,52,96,0) 80%),
    radial-gradient(ellipse 30% 60% at 10% 30%,rgba(200,192,178,.9),rgba(200,192,178,0) 80%),
    linear-gradient(160deg,#d6d0c4,#9b968e 45%,#3a4a70 100%)" role="img" aria-label="Smiling man in a navy suit wearing black glasses, talking on a phone"></div>
  <div class="band">Mens Frames</div>
</section>
<section class="abs category" style="left:621px">
  <div class="photo" style="inset:0;background:
    radial-gradient(ellipse 26% 22% at 40% 32%,rgba(220,180,158,.9),rgba(220,180,158,0) 75%),
    radial-gradient(ellipse 60% 45% at 45% 95%,rgba(28,26,26,.95),rgba(28,26,26,0) 80%),
    radial-gradient(ellipse 35% 50% at 85% 45%,rgba(170,172,176,.9),rgba(170,172,176,0) 80%),
    linear-gradient(160deg,#c7c2b8,#8e7f72 45%,#2c2a2a 100%)" role="img" aria-label="Woman in a leather jacket adjusting round glasses on a city street"></div>
  <div class="band">Womens Frames</div>
</section>

<h2 class="abs section-title" style="left:0;width:1200px;text-align:center;top:1282px">Fretured Products</h2>
<div class="abs" style="left:1036px;top:1286px;display:flex;gap:9px">
  <div class="arrow-btn"><svg width="10" height="12" viewBox="0 0 10 12"><path d="M7 1L2 6l5 5" fill="none" stroke="#1b1b1b" stroke-width="2"/></svg></div>
  <div class="arrow-btn"><svg width="10" height="12" viewBox="0 0 10 12"><path d="M3 1l5 5-5 5" fill="none" stroke="#1b1b1b" stroke-width="2"/></svg></div>
</div>
<nav class="abs tabs"><span class="active">All Frames</span><span class="sep">|</span><span>Best Sellers</span><span class="sep">|</span><span>New Arrivals</span></nav>

<article class="abs product" style="left:42px">
  <div class="photo frame" style="background:radial-gradient(ellipse 42% 20% at 50% 48%,rgba(190,176,150,.75),rgba(245,245,245,0) 80%)" role="img" aria-label="Thin gold round metal frame"></div>
  <div class="tool" style="left:70px"><svg width="16" height="14" viewBox="0 0 16 14"><path d="M8 13L2 7a3.3 3.3 0 0 1 6-4 3.3 3.3 0 0 1 6 4z" fill="none" stroke="#fff" stroke-width="1.6"/></svg></div>
  <div class="tool" style="left:110px"><svg width="16" height="14" viewBox="0 0 16 14" fill="none" stroke="#fff" stroke-width="1.6"><path d="M1 1h2l2 8h8l2-6H4"/><circle cx="6" cy="12" r="1"/><circle cx="12" cy="12" r="1"/></svg></div>
  <div class="tool" style="left:150px"><svg width="12" height="14" viewBox="0 0 12 14" fill="none" stroke="#fff" stroke-width="1.6"><rect x="1" y="1" width="10" height="12"/><path d="M3 5h6M3 8h6"/></svg></div>
</article>
<article class="abs product" style="left:328px"><div class="photo frame" style="background:radial-gradient(ellipse 42% 20% at 50% 50%,rgba(140,104,58,.7),rgba(245,245,245,0) 80%)" role="img" aria-label="Tortoiseshell acetate frame"></div></article>
<article class="abs product" style="left:614px"><div class="photo frame" style="background:radial-gradient(ellipse 42% 20% at 50% 50%,rgba(96,36,44,.7),rgba(245,245,245,0) 80%)" role="img" aria-label="Burgundy and black acetate frame"></div></article>
<article class="abs product" style="left:897px"><div class="photo frame" style="background:radial-gradient(ellipse 42% 20% at 50% 50%,rgba(27,27,27,.7),rgba(245,245,245,0) 80%)" role="img" aria-label="Black round acetate frame"></div></article>

<div class="abs product-meta" style="left:42px">Product Name<br><b>$ 00.00</b></div>
<div class="abs product-meta" style="left:328px">Product Name<br><b>$ 00.00</b></div>
<div class="abs product-meta" style="left:614px">Product Name<br><b>$ 00.00</b></div>
<div class="abs product-meta" style="left:897px">Product Name<br><b>$ 00.00</b></div>
<a class="btn" style="left:502px;top:1759px;width:186px;height:33px">Shop Now</a>

<section class="abs lens-offer"></section>
<h2 class="abs lens-title">Contact Lenses</h2>
<p class="abs lens-sub">lenses starting</p>
<p class="abs lens-price">at $79</p>
<a class="btn" style="left:119px;top:2137px;width:189px;height:33px">Shop Now</a>
<div class="photo lens-photo" role="img" aria-label="Black rectangular glasses frame with a pair of clear replacement lenses below"></div>

<h2 class="abs section-title" style="left:75px;width:487px;text-align:center;top:2364px;font-size:26px;font-weight:500">Reviews Customers</h2>
<section class="abs review-card"></section>
<div class="photo avatar" role="img" aria-label="Customer portrait in sunglasses"></div>
<div class="abs reviewer" style="top:2622px;font:700 18px 'Lato',sans-serif;color:var(--ink)">Dorian Vale</div>
<div class="abs reviewer" style="top:2647px;font:400 14px 'Lato',sans-serif;color:var(--red)">Sports Person</div>
<p class="abs reviewer" style="top:2674px;left:130px;width:377px;font:400 14px/19px 'Lato',sans-serif;color:var(--mid)">Lorem Ipsum is simply dummy text of the printing typesetting industry. Lorem Ipsum has been the industry's standard dummy</p>
<span class="abs quote" style="left:134px;top:2620px">&ldquo;</span>
<span class="abs quote" style="left:418px;top:2728px">&rdquo;</span>
<div class="abs reviewer" style="top:2736px;font:400 20px 'Lato',sans-serif;color:var(--star);letter-spacing:1px">★★★★★</div>
<div class="abs dots"><i class="on"></i><i></i><i></i></div>

<h2 class="abs section-title" style="left:631px;top:2364px;font-size:26px;font-weight:500">Our Blog</h2>
<div class="abs" style="left:1074px;top:2370px;display:flex;gap:4px">
  <svg width="18" height="18" viewBox="0 0 18 18"><circle cx="9" cy="9" r="8" fill="none" stroke="#1b1b1b" stroke-width="1.5"/><path d="M11 5L7 9l4 4" fill="none" stroke="#1b1b1b" stroke-width="1.5"/></svg>
  <svg width="18" height="18" viewBox="0 0 18 18"><circle cx="9" cy="9" r="8" fill="none" stroke="#3276b5" stroke-width="1.5"/><path d="M7 5l4 4-4 4" fill="none" stroke="#3276b5" stroke-width="1.5"/></svg>
</div>
<article class="abs post" style="top:2425px">
  <div class="photo thumb" style="background:radial-gradient(ellipse 45% 50% at 50% 55%,rgba(196,150,124,.9),rgba(196,150,124,0) 80%),linear-gradient(135deg,#2e2e2e,#6b5448 60%,#3f4249)" role="img" aria-label="Close portrait of a man wearing glasses"></div>
  <h3>Blog Tile Heading 01</h3>
  <div class="by"><span><b>By</b> Mira Coleby</span><span>january 19, 2019</span></div>
  <p>Lorem Ipsum is simply dummy text of the printing and typesetting industry. Lorem Ipsum has been the industry's.</p>
  <div class="more">Read More... <svg width="12" height="12" viewBox="0 0 12 12"><circle cx="6" cy="6" r="5" fill="none" stroke="#474747"/><path d="M5 4l2 2-2 2" fill="none" stroke="#474747"/></svg></div>
</article>
<article class="abs post" style="top:2619px">
  <div class="photo thumb" style="background:radial-gradient(ellipse 40% 45% at 50% 50%,rgba(206,160,140,.85),rgba(206,160,140,0) 80%),linear-gradient(135deg,#241f1e,#5e3f38 55%,#8a6a5c)" role="img" aria-label="Close portrait of a woman wearing glasses"></div>
  <h3>Blog Title Heading 02</h3>
  <div class="by"><span><b>By</b> Tobias Wren</span><span>january 19, 2019</span></div>
  <p>Lorem Ipsum is simply dummy text of the printing and typesetting industry. Lorem Ipsum has been the industry's.</p>
  <div class="more">Read More... <svg width="12" height="12" viewBox="0 0 12 12"><circle cx="6" cy="6" r="5" fill="none" stroke="#474747"/><path d="M5 4l2 2-2 2" fill="none" stroke="#474747"/></svg></div>
</article>
<a class="btn" style="left:813px;top:2823px;width:188px;height:32px">View More</a>

<h2 class="abs news-title">Join The Newletter</h2>
<p class="abs news-sub">Sign up for Our Newsletter</p>
<form class="abs news-form"><span>Email here</span><b>Subscribe</b></form>

<div class="abs service" style="left:117px;width:305px">
  <svg class="abs" style="left:123px;top:30px" width="60" height="46" viewBox="0 0 60 46"><path d="M2 22l6-2 8 6 14-3L18 4l7-2 20 18 11-3c3 0 4 3 1 4L12 33z" fill="#1b1b1b"/></svg>
  <h4>Free Shipping Worldwide</h4><p>Order Over USD 15-7days week</p>
</div>
<div class="abs service featured" style="left:447px;width:303px">
  <svg class="abs" style="left:130px;top:26px" width="44" height="48" viewBox="0 0 44 48" fill="#fff"><rect x="4" y="2" width="30" height="20" rx="3"/><path d="M10 22l-2 7 8-7z"/><circle cx="26" cy="32" r="6"/><path d="M14 48c0-9 5-12 12-12s12 3 12 12z"/><path d="M10 8h18M10 14h12" stroke="#3276b5" stroke-width="2.5"/></svg>
  <h4>24/7 Customer Services</h4><p>Call us 24/7 at 000 555 0199</p>
</div>
<div class="abs service" style="left:773px;width:303px">
  <svg class="abs" style="left:132px;top:28px" width="40" height="44" viewBox="0 0 40 44"><path d="M20 2a18 16 0 1 1-9 30l-7 6 2-10A18 16 0 0 1 20 2z" fill="#1b1b1b"/><text x="20" y="25" text-anchor="middle" font-family="Roboto,sans-serif" font-weight="700" font-size="18" fill="#fff">?</text></svg>
  <h4>Product Guide</h4><p>How to Shop</p>
</div>

<footer class="abs site-footer"></footer>
<div class="abs foot-brand" style="color:var(--white)">VORAN</div>
<p class="abs foot-about" style="color:var(--white)">Lorem Ipsum is simply dummy text the printing and ypesetting industry. has been the industry's standard dummy...</p>
<div class="abs cards"><i></i><i></i><i></i><i></i></div>

<h4 class="abs foot-head" style="left:449px;color:var(--white)">Information</h4>
<ul class="abs foot-list" style="left:452px;color:var(--white)">
  <li>Track Order</li><li>About Us</li><li>Contact Us</li><li>Returns</li><li>Warranty</li><li>FAQ</li>
</ul>

<h4 class="abs foot-head" style="left:626px;color:var(--white)">Address</h4>
<div class="abs addr" style="left:600px;color:var(--white)">
  <div><svg width="12" height="15" viewBox="0 0 12 15" style="margin-top:3px"><path d="M6 0a6 6 0 0 1 6 6c0 4-6 9-6 9S0 10 0 6a6 6 0 0 1 6-6z" fill="#fff"/><circle cx="6" cy="6" r="2" fill="#333"/></svg><span>48 Larchmont Row<br>Fenwick, USA<br>Zip :1234</span></div>
  <div><svg width="12" height="12" viewBox="0 0 12 12" style="margin-top:4px"><path d="M2 0h3l1 3-2 1a7 7 0 0 0 4 4l1-2 3 1v3c0 1-1 2-2 2A11 11 0 0 1 0 2c0-1 1-2 2-2z" fill="#fff"/></svg><span>+100 555 0142</span></div>
  <div><svg width="12" height="10" viewBox="0 0 12 10" style="margin-top:5px"><rect width="12" height="10" fill="#fff"/><path d="M0 0l6 5 6-5" fill="none" stroke="#333"/></svg><span>info@voran.com</span></div>
</div>

<h4 class="abs foot-head" style="left:842px;color:var(--white)">Quick Contact</h4>
<div class="field" style="left:842px;top:3487px;width:114px;height:24px">Name</div>
<div class="field" style="left:962px;top:3487px;width:114px;height:24px">Phone</div>
<div class="field" style="left:842px;top:3517px;width:234px;height:56px">Message</div>
<div class="abs send" style="color:var(--white)">SEND</div>

<p class="abs copyright">Copyright © 2019 Voran. All Rights Reserved.</p>
<div class="abs social"><i></i><i></i><i></i><i></i><i></i></div>

</body>
</html>
```